ORLUq Business card. A.I. company developing trading strategies.

My name is tommaso fabbri and I'm CEO and co-founder of ORLUQ Research, an AI company focusing on generating Ai-driven trading strategies.
This is our website: https://orluq-research.example/
Values of our company: tech & R&D driven (we're all very mathy/stats/data driven), sophisticated (we only look for sophisticated, high knowledge investors), reserved (we don't go around telling anyone what we do).
Our main product: KobraFNX. A trading strategy that delivered 70% in 2022 and 20% in 2023 so far.
Our main potential clients: HNW individuals, hedge funds, asset managers, tech entrepreneur.
Hedge funds, asset managers, High Net Worth individuals, Pension funds
The basic: name, job title, company name, address, mail, phone number

```html
<!DOCTYPE html>
<html lang="en">
<head>
<meta charset="utf-8">
<title>ORLUq Research – Business Card</title>
<link rel="stylesheet" href="https://fonts.googleapis.com/css2?family=Poppins:wght@300;400;600&display=swap">
<style>
  :root {
    --stage: #2b2b2d;
    --card-dark: #1c1d1f;
    --crimson: #c8002f;
    --crimson-deep: #b40029;
    --white: #ffffff;
    --rule: #5a5b5e;
  }
  * { box-sizing: border-box; margin: 0; padding: 0; }
  html, body {
    width: 1200px; height: 1108px; overflow: hidden;
    background: var(--stage);
    font-family: "Poppins", sans-serif;
  }
  .stage {
    position: relative; width: 1200px; height: 1108px;
    display: flex; justify-content: center; align-items: center; gap: 70px;
  }
  .card {
    width: 460px; height: 760px; border-radius: 26px;
    position: relative; overflow: hidden;
    box-shadow: 0 18px 40px rgba(0,0,0,.45);
  }
  .card--front {
    background: var(--card-dark);
    display: flex; flex-direction: column; align-items: center;
    padding-bottom: 60px;
    color: var(--white); text-align: center;
  }
  .wordmark {
    margin-top: 120px;
    display: flex; align-items: center; gap: 14px;
    font-weight: 300; font-size: 84px; letter-spacing: 4px; line-height: 1;
    color: var(--white);
  }
  .wordmark__dot {
    width: 12px; height: 12px; border-radius: 50%; background: var(--crimson);
  }
  .holder { margin-top: auto; }
  .holder__name {
    color: var(--crimson); font-weight: 600; font-size: 32px; letter-spacing: 1px; line-height: 1.1;
  }
  .holder__title { font-size: 24px; font-weight: 400; margin-top: 4px; }
  .contact-icons {
    margin-top: 20px; width: 300px;
    display: flex; align-items: center; gap: 8px;
  }
  .contact-icons .rule { flex: 1; height: 1px; background: var(--rule); }
  .icon {
    width: 40px; height: 40px; border-radius: 6px; background: var(--crimson);
    display: flex; align-items: center; justify-content: center;
  }
  .contact { margin-top: 10px; font-size: 22px; line-height: 1.32; }
  .divider { width: 300px; height: 1px; background: var(--rule); margin: 14px 0 12px; }
  .company { color: var(--crimson); font-size: 22px; line-height: 1.3; }
  .address { font-size: 22px; line-height: 1.3; }
  .card--back { background: var(--crimson); }
  .back-texture {
    position: absolute; inset: 0;
    background: linear-gradient(160deg, var(--crimson) 0%, var(--crimson-deep) 100%);
  }
  .back-mark {
    position: absolute; inset: 0;
    display: flex; align-items: center; justify-content: center; gap: 8px;
    font-weight: 300; font-size: 46px; letter-spacing: 3px; color: var(--white);
  }
  .back-mark .wordmark__dot { width: 7px; height: 7px; background: var(--white); }
</style>
</head>
<body>
<main class="stage">
  <section class="card card--front">
    <div class="wordmark"><span>ORLUq</span><span class="wordmark__dot"></span></div>

    <div class="holder">
      <p class="holder__name">FABBRI</p>
      <p class="holder__title">CEO and Co-founder</p>
    </div>

    <div class="contact-icons">
      <span class="rule"></span>
      <span class="icon" aria-label="Phone">
        <svg width="24" height="24" viewBox="0 0 24 24"><path d="M6.6 10.8a15 15 0 0 0 6.6 6.6l2.2-2.2a1 1 0 0 1 1-.25 11.4 11.4 0 0 0 3.6.57 1 1 0 0 1 1 1V20a1 1 0 0 1-1 1A17 17 0 0 1 3 4a1 1 0 0 1 1-1h3.5a1 1 0 0 1 1 1c0 1.25.2 2.450.57 3.57a1 1 0 0 1-.25 1z" fill="#1c1d1f"/></svg>
      </span>
      <span class="icon" aria-label="Email">
        <svg width="24" height="24" viewBox="0 0 24 24"><rect x="3" y="6" width="18" height="12" rx="1" fill="#1c1d1f"/><path d="M3.5 6.5 12 13l8.5-6.5" stroke="#c8002f" stroke-width="1.5" fill="none"/></svg>
      </span>
      <span class="icon" aria-label="Website">
        <svg width="24" height="24" viewBox="0 0 24 24"><circle cx="12" cy="12" r="9" fill="#1c1d1f"/><path d="M3 12h18M12 3c3 3 3 15 0 18M12 3c-3 3-3 15 0 18" stroke="#c8002f" stroke-width="1.3" fill="none"/></svg>
      </span>
      <span class="rule"></span>
    </div>

    <div class="contact">
      <p>555014728</p>
      <p>office@orluqresearch.example</p>
      <p>www.orluq-research.example</p>
    </div>

    <div class="divider"></div>

    <p class="company">Orluq Research</p>
    <p class="address">14 Rue des Lilas Vertes</p>
    <p class="address">75011 PARIS 11</p>
  </section>

  <section class="card card--back">
    <div class="back-texture" role="img" aria-label="Tone-on-tone repeating brand pattern across the red card back"></div>
    <div class="back-mark"><span>ORLUq</span><span class="wordmark__dot"></span></div>
  </section>
</main>
</body>
</html>
```